Home Security Website

This website is for a home security website. We feature the best in home security products and monitoring. The website name is Porchlight Partners.
We would like a direct response design with a large hero image.
The final design should incorporate safety, security, and family. Please do not use scare tactics in the design.
Target Market(s)
Women, primarily
Industry/Entity Type
Security
Requirements
Must have
- Must have a clear Call to Action Area for telephone and lead gen form
Nice to have
- - Large heroes with lifestyle images of family - security
- below the fold text area with boxes
Should not have
- no scare tactics please
DO NOT submit designs with DARK or BLACK backgrounds

```html
<!DOCTYPE html>
<html lang="en">
<head>
<meta charset="utf-8">
<title>Porchlight Partners – Home Security</title>
<link href="https://fonts.googleapis.com/css2?family=Roboto:wght@400;500;700&family=Oswald:wght@500;700&display=swap" rel="stylesheet">
<style>
:root{
  --red:#d8191c;
  --red-dark:#b01014;
  --red-light:#ee3b3b;
  --ink:#2b2b2b;
  --muted:#6a6a6a;
  --page:#f1f1f1;
  --white:#ffffff;
  --panel:#3a3a3a;
  --yellow:#f5b400;
  --yellow-light:#ffd23a;
  --line:#dcdcdc;
}
*{box-sizing:border-box;margin:0;padding:0}
html,body{width:1200px;height:1027px;overflow:hidden}
body{background:var(--page);font-family:Roboto,Arial,sans-serif;color:var(--ink);position:relative}
.abs{position:absolute}

/* header */
.site-header{left:0;top:0;width:1200px;height:115px;background:linear-gradient(#fafafa,#ececec)}
.brand{left:157px;top:36px;display:flex;align-items:center;gap:10px}
.brand-mark{width:44px;height:44px;background:var(--ink);border-radius:4px}
.brand-name{font-family:Oswald,Arial,sans-serif;font-weight:700;font-size:27px;line-height:1;color:var(--red);text-transform:uppercase;white-space:nowrap}
.brand-name span{display:block;font-size:15px;color:var(--red)}
.search{left:498px;top:46px;width:274px;height:36px;border-radius:18px;background:var(--white);border:1px solid #d4d4d4;box-shadow:0 3px 5px rgba(0,0,0,.12) inset}
.search-label{left:16px;top:10px;font-size:12px;font-style:italic;color:#999}
.search-btn{right:9px;top:7px;width:22px;height:22px;border-radius:50%;background:var(--yellow)}
.contact{left:878px;top:34px;width:240px;white-space:nowrap}
.contact-line{font-size:11px;color:var(--muted);line-height:15px;padding-left:24px}
.contact-phone{font-size:27px;line-height:32px;font-weight:500;color:var(--red);padding-left:24px;margin-top:3px;letter-spacing:.5px}
.contact svg{position:absolute;left:0}

/* nav */
.main-nav{left:0;top:115px;width:1200px;height:42px;background:linear-gradient(var(--red-light),var(--red-dark))}
.nav-home{left:160px;top:5px;width:66px;height:32px;border-radius:16px;background:#1e1e1e;display:flex;align-items:center;justify-content:center}
.nav-list{left:240px;top:0;display:flex;list-style:none;height:42px}
.nav-list li{color:var(--white);font-family:Oswald,Arial,sans-serif;font-weight:500;font-size:16px;letter-spacing:1px;line-height:42px;width:130px;text-align:center;border-left:1px solid rgba(0,0,0,.18)}
.nav-list li:first-child{border-left:none}

/* hero */
.hero{left:0;top:157px;width:1200px;height:371px;background:linear-gradient(180deg,#b9c4cc 0%,#d8cdbb 35%,#b9a78c 70%,#c9a84a 100%)}
.hero-dots{left:162px;top:507px;display:flex;gap:5px}
.hero-dots i{width:9px;height:9px;border-radius:50%;background:var(--white);display:block}
.hero-dots i.on{background:var(--red);border:2px solid var(--white)}
.consult{left:787px;top:157px;width:256px;height:371px;background:linear-gradient(#404040,#2e2e2e)}
.consult h2{font-family:Oswald,Arial,sans-serif;font-weight:500;color:var(--yellow-light);font-size:21px;text-align:center;margin-top:14px;letter-spacing:.3px}
.consult p.lead{color:#e0e0e0;font-size:10px;text-align:center;margin-top:2px}
.field{left:20px;width:216px;height:28px;border-radius:14px;background:var(--white);border:2px solid #cfcfcf}
.field svg{position:absolute;left:7px;top:6px}
.q{left:0;width:256px;top:257px;color:var(--white);font-size:12px;font-weight:500;text-align:center}
.radios{left:0;width:256px;top:277px;display:flex;justify-content:center;gap:22px;color:#eee;font-size:11px}
.radios span{display:flex;align-items:center;gap:5px}
.radios i{width:11px;height:11px;border-radius:50%;background:var(--white);display:block}
.radios i.on{border:3px solid var(--red)}
.submit{left:20px;top:302px;width:216px;height:44px;border-radius:22px;background:linear-gradient(var(--yellow-light),var(--yellow));color:var(--white);font-family:Oswald,Arial,sans-serif;font-weight:700;font-size:26px;text-align:center;line-height:44px;letter-spacing:1px;box-shadow:0 2px 3px rgba(0,0,0,.4)}

/* welcome */
.welcome{left:0;top:528px;width:1200px;height:132px;background:var(--white)}
.welcome h1{font-size:15px;font-weight:700;text-align:center;margin-top:22px;color:var(--ink)}
.welcome h1 span{color:var(--red)}
.welcome p{width:890px;margin:9px auto 0;font-size:12px;line-height:19px;color:var(--muted);text-align:center}
.divider{left:200px;top:658px;width:800px;height:8px;background:radial-gradient(ellipse at top,rgba(0,0,0,.18),transparent 70%)}

/* feature boxes */
.feature{top:705px;width:281px;height:203px;background:linear-gradient(#fafafa,#e9e9e9);border:1px solid var(--line);box-shadow:0 3px 4px rgba(0,0,0,.1)}
.feature h3{height:40px;background:linear-gradient(var(--red-light),var(--red-dark));color:var(--white);font-size:17px;font-weight:500;line-height:40px;padding-left:16px}
.feature ul{list-style:none;position:absolute;left:16px;top:60px;z-index:1}
.feature li{font-size:10.5px;color:var(--ink);line-height:16px;display:flex;align-items:center;gap:5px;white-space:nowrap}
.feature li svg{flex:none}
.more{left:16px;top:154px;width:70px;height:18px;border-radius:9px;background:var(--red);color:var(--white);font-size:8.5px;font-weight:700;line-height:18px;padding-left:9px}
.more::after{content:"";position:absolute;right:7px;top:6px;border:3px solid transparent;border-left:4px solid var(--white)}
.feature-img{right:10px;top:44px;width:105px;height:155px;border-radius:6px}

/* footer */
.site-footer{left:0;top:954px;width:1200px;height:73px;background:linear-gradient(#fdfdfd,#efefef);border-top:1px solid #e2e2e2}
.footer-links{left:157px;top:24px;font-size:10.5px;color:var(--muted);display:flex;gap:8px}
.footer-links b{font-weight:400;color:#aaa}
.copy{left:157px;top:43px;font-size:10px;color:#888}
.footer-brand{left:972px;top:22px;display:flex;align-items:center;gap:5px;font-family:Oswald,Arial,sans-serif;font-weight:500;font-size:15px;color:#a9a9a9;text-transform:uppercase;white-space:nowrap}
.footer-brand i{width:18px;height:18px;background:#b5b5b5;display:block}
</style>
</head>
<body>

<header class="site-header abs">
  <div class="brand abs">
    <div class="brand-mark"></div>
    <div class="brand-name">Porchlight<span>Partners</span></div>
  </div>
  <div class="search abs">
    <span class="search-label abs">Search here...</span>
    <span class="search-btn abs"></span>
  </div>
  <div class="contact abs">
    <svg width="12" height="16" viewBox="0 0 12 16" style="top:1px"><path d="M6 0a6 6 0 0 1 6 6c0 4-6 10-6 10S0 10 0 6a6 6 0 0 1 6-6z" fill="#9a9a9a"/><circle cx="6" cy="6" r="2.2" fill="#f3f3f3"/></svg>
    <div class="contact-line">Porchlight Partners LTD<br>1480 Alder Lane, Riverton</div>
    <svg width="11" height="16" viewBox="0 0 11 16" style="top:42px"><rect x="0" y="0" width="11" height="16" rx="2" fill="#9a9a9a"/><rect x="2" y="2" width="7" height="9" fill="#f3f3f3"/></svg>
    <div class="contact-phone">55-555-0147</div>
  </div>
</header>

<nav class="main-nav abs">
  <div class="nav-home abs">
    <svg width="20" height="18" viewBox="0 0 20 18"><path d="M10 0 20 9h-3v9h-5v-6H8v6H3V9H0z" fill="#fff"/></svg>
  </div>
  <ul class="nav-list abs">
    <li>COMPANY</li><li>SERVICES</li><li>CLIENTS</li><li>PRODUCTS</li><li>OUR BLOG</li><li>CONTACTS</li>
  </ul>
</nav>

<section class="hero abs" role="img" aria-label="Smiling family relaxing on the lawn in front of their suburban brick home"></section>
<div class="hero-dots abs"><i></i><i class="on"></i><i></i></div>

<aside class="consult abs">
  <h2>SECURITY CONSULTATION</h2>
  <p class="lead">Get a free security consultation for your home.</p>
  <div class="field abs" style="top:74px"><svg width="14" height="14" viewBox="0 0 14 14"><circle cx="7" cy="4" r="3.5" fill="#222"/><path d="M0 14c0-4 3-6 7-6s7 2 7 6z" fill="#222"/></svg></div>
  <div class="field abs" style="top:110px"><svg width="14" height="12" viewBox="0 0 14 12" style="top:7px"><rect width="14" height="11" fill="#222"/><path d="M0 0l7 6 7-6" stroke="#fff" fill="none"/></svg></div>
  <div class="field abs" style="top:146px"><svg width="11" height="15" viewBox="0 0 12 16"><path d="M6 0a6 6 0 0 1 6 6c0 4-6 10-6 10S0 10 0 6a6 6 0 0 1 6-6z" fill="#222"/><circle cx="6" cy="6" r="2.2" fill="#fff"/></svg></div>
  <div class="field abs" style="top:182px;width:60px"><svg width="10" height="14" viewBox="0 0 11 16"><rect width="11" height="16" rx="2" fill="#222"/><rect x="2" y="2" width="7" height="8" fill="#fff"/></svg></div>
  <div class="field abs" style="top:182px;left:84px;width:152px"></div>
  <div class="field abs" style="top:218px"></div>
  <div class="q abs">Are You A Homeowner?</div>
  <div class="radios abs"><span><i class="on"></i>Yes</span><span><i></i>No</span></div>
  <div class="submit abs">SUBMIT</div>
</aside>

<section class="welcome abs">
  <h1>WELCOME TO <span>PORCHLIGHT PARTNERS</span></h1>
  <p>Lorem Ipsum is simply dummy text of the printing and typesetting industry. Lorem Ipsum has been the industry's standard dummy text ever since the 1500s, when an unknown printer took a galley of type and scrambled it to make a type specimen book. It has survived not only five centuries, but also the leap into electronic typesetting, remaining essentially unchanged. It was popularised in the 1960s with the release of Letraset sheets containing...</p>
</section>
<div class="divider abs"></div>

<article class="feature abs" style="left:156px">
  <h3>SAFETY</h3>
  <ul>
    <li><svg width="9" height="9" viewBox="0 0 9 9"><rect width="9" height="9" fill="#fff" stroke="#bbb"/><path d="M2 4.5l2 2 3.5-4" stroke="#2a7fc9" stroke-width="1.4" fill="none"/></svg>Lorem Ipsum is simply</li>
    <li><svg width="9" height="9" viewBox="0 0 9 9"><rect width="9" height="9" fill="#fff" stroke="#bbb"/><path d="M2 4.5l2 2 3.5-4" stroke="#2a7fc9" stroke-width="1.4" fill="none"/></svg>Dummy text of the printing</li>
    <li><svg width="9" height="9" viewBox="0 0 9 9"><rect width="9" height="9" fill="#fff" stroke="#bbb"/><path d="M2 4.5l2 2 3.5-4" stroke="#2a7fc9" stroke-width="1.4" fill="none"/></svg>Typesetting industry</li>
    <li><svg width="9" height="9" viewBox="0 0 9 9"><rect width="9" height="9" fill="#fff" stroke="#bbb"/><path d="M2 4.5l2 2 3.5-4" stroke="#2a7fc9" stroke-width="1.4" fill="none"/></svg>Lorem Ipsum has been</li>
    <li><svg width="9" height="9" viewBox="0 0 9 9"><rect width="9" height="9" fill="#fff" stroke="#bbb"/><path d="M2 4.5l2 2 3.5-4" stroke="#2a7fc9" stroke-width="1.4" fill="none"/></svg>Industry's standard dummy</li>
  </ul>
  <div class="more abs">Learn More</div>
  <div class="feature-img abs" role="img" aria-label="Two fingers with drawn guard figures" style="background:linear-gradient(#f0e4dc,#d9b9a5)"></div>
</article>

<article class="feature abs" style="left:460px">
  <h3>SECURITY</h3>
  <ul>
    <li><svg width="9" height="9" viewBox="0 0 9 9"><rect width="9" height="9" fill="#fff" stroke="#bbb"/><path d="M2 4.5l2 2 3.5-4" stroke="#2a7fc9" stroke-width="1.4" fill="none"/></svg>Lorem Ipsum is simply</li>
    <li><svg width="9" height="9" viewBox="0 0 9 9"><rect width="9" height="9" fill="#fff" stroke="#bbb"/><path d="M2 4.5l2 2 3.5-4" stroke="#2a7fc9" stroke-width="1.4" fill="none"/></svg>Dummy text of the printing</li>
    <li><svg width="9" height="9" viewBox="0 0 9 9"><rect width="9" height="9" fill="#fff" stroke="#bbb"/><path d="M2 4.5l2 2 3.5-4" stroke="#2a7fc9" stroke-width="1.4" fill="none"/></svg>Typesetting industry</li>
    <li><svg width="9" height="9" viewBox="0 0 9 9"><rect width="9" height="9" fill="#fff" stroke="#bbb"/><path d="M2 4.5l2 2 3.5-4" stroke="#2a7fc9" stroke-width="1.4" fill="none"/></svg>Lorem Ipsum has been</li>
    <li><svg width="9" height="9" viewBox="0 0 9 9"><rect width="9" height="9" fill="#fff" stroke="#bbb"/><path d="M2 4.5l2 2 3.5-4" stroke="#2a7fc9" stroke-width="1.4" fill="none"/></svg>Industry's standard dummy</li>
  </ul>
  <div class="more abs">Learn More</div>
  <div class="feature-img abs" role="img" aria-label="Hand holding a small model house" style="background:linear-gradient(#f4f4f4,#e2cfc6)"></div>
</article>

<article class="feature abs" style="left:764px">
  <h3>How It Works</h3>
  <ul>
    <li><svg width="9" height="9" viewBox="0 0 9 9"><rect width="9" height="9" fill="#fff" stroke="#bbb"/><path d="M2 4.5l2 2 3.5-4" stroke="#2a7fc9" stroke-width="1.4" fill="none"/></svg>Lorem Ipsum is simply</li>
    <li><svg width="9" height="9" viewBox="0 0 9 9"><rect width="9" height="9" fill="#fff" stroke="#bbb"/><path d="M2 4.5l2 2 3.5-4" stroke="#2a7fc9" stroke-width="1.4" fill="none"/></svg>Dummy text of the printing</li>
    <li><svg width="9" height="9" viewBox="0 0 9 9"><rect width="9" height="9" fill="#fff" stroke="#bbb"/><path d="M2 4.5l2 2 3.5-4" stroke="#2a7fc9" stroke-width="1.4" fill="none"/></svg>Typesetting industry</li>
    <li><svg width="9" height="9" viewBox="0 0 9 9"><rect width="9" height="9" fill="#fff" stroke="#bbb"/><path d="M2 4.5l2 2 3.5-4" stroke="#2a7fc9" stroke-width="1.4" fill="none"/></svg>Lorem Ipsum has been</li>
    <li><svg width="9" height="9" viewBox="0 0 9 9"><rect width="9" height="9" fill="#fff" stroke="#bbb"/><path d="M2 4.5l2 2 3.5-4" stroke="#2a7fc9" stroke-width="1.4" fill="none"/></svg>Industry's standard dummy</li>
  </ul>
  <div class="more abs">Learn More</div>
  <div class="feature-img abs" role="img" aria-label="Surprised man in glasses pointing at the list" style="background:linear-gradient(#f3f3f3,#d8d8d8)"></div>
</article>

<footer class="site-footer abs">
  <div class="footer-links abs">Home <b>|</b> About US <b>|</b> Terms of Service <b>|</b> Privacy Policy <b>|</b> Contact Us</div>
  <div class="copy abs">Copyrights © 2013. PorchlightPartners.com.</div>
  <div class="footer-brand abs"><i></i>Porchlight Partners</div>
</footer>

</body>
</html>
```